Project management consultancy needs a website designed

Our company (Meridale PMO) currently has a website (http://www.meridalepmo-example.com.au) that needs to be re-designed and enhanced. Company is a professional services/consultancy business focused on project management. We are looking for something more professional. It would be advantageous if the website can be hosted in SharePoint. We are reasonably happy with the content, what we're after is something that has better aesthetics. Attached to the brief is a copy of our logo in vector format.

Target Market(s)

Small to medium businesses

Industry/Entity Type

It Company

Contact Information for Business Card

logo/company name on back, contact details plus smaller logo on front. Information to display = Name, title, address, phone number, email address, website address

Coding

Coded - Design and coding required

Number of Pages Required

4 page

Font styles to use
Sans Serif

Requirements
Must have
• Website must have: A home page, content page, contact details page (including a contact us function), blog. Project management related images/photos
Nice to have
• Website has the ability to support video content

```html
<!DOCTYPE html>
<html lang="en">
<head>
<meta charset="utf-8">
<title>Meridale PMO</title>
<link href="https://fonts.googleapis.com/css2?family=Oswald:wght@300;400;500&family=Roboto:wght@400;500&family=Open+Sans:wght@400;600&display=swap" rel="stylesheet">
<style>
:root{
  --blue:#1a5bc4;
  --blue-dark:#134aa6;
  --nav-active:#3a3a3a;
  --ink:#222;
  --text:#555;
  --muted:#777;
  --light:#f3f4f6;
  --white:#fff;
}
*{box-sizing:border-box;margin:0;padding:0}
html,body{width:675px;height:1200px;overflow:hidden;background:var(--white)}
body{position:relative;font-family:'Open Sans',sans-serif;color:var(--text)}
.abs{position:absolute}
/* header */
.brand{left:55px;top:22px;display:flex;align-items:center;gap:8px}
.brand-mark{width:30px;height:30px;background:var(--blue);border-radius:4px}
.brand-name{font-family:'Roboto',sans-serif;font-size:19px;color:var(--blue);font-weight:500;letter-spacing:.3px}
.contact-head{left:497px;top:22px;display:flex;gap:10px;align-items:flex-start}
.phone-ring{width:24px;height:24px;border:1px solid #333;border-radius:50%;display:flex;align-items:center;justify-content:center;margin-top:2px}
.contact-head .ph{font-family:'Roboto',sans-serif;font-size:11px;color:var(--ink)}
.contact-head .em{font-size:7.5px;color:#444;margin-top:3px}
/* nav */
.nav{left:0;top:74px;width:675px;height:31px;background:var(--blue);display:flex;padding-left:55px}
.nav a{font-family:'Roboto',sans-serif;font-size:8px;color:var(--white);text-decoration:none;padding:0 14px;line-height:31px;border-right:1px solid rgba(255,255,255,.12)}
.nav a.active{background:var(--nav-active);padding:0 15px}
/* hero */
.hero{left:0;top:105px;width:675px;height:299px;background:linear-gradient(100deg,#eef1f4 0%,#dde3ea 35%,#c9b6a3 60%,#8b7a6d 85%,#5d5450 100%)}
.hero-title{left:64px;top:182px;font-family:'Oswald',sans-serif;font-weight:400;font-size:42px;line-height:46px;color:var(--white);-webkit-text-stroke:1px #4c7fc9;paint-order:stroke fill;text-shadow:0 1px 2px rgba(40,80,150,.35);letter-spacing:-1.5px}
.hero-title .small{font-size:33px;letter-spacing:-1px}
.btn{background:var(--blue);color:var(--white);font-family:'Roboto',sans-serif;font-size:8px;display:flex;align-items:center;justify-content:center;border-radius:2px}
.hero-btn{left:63px;top:278px;width:104px;height:27px;font-size:8.5px;box-shadow:0 1px 2px rgba(0,0,0,.3)}
.arrow{width:20px;height:20px;border-radius:50%;background:rgba(60,60,60,.55);display:flex;align-items:center;justify-content:center;top:245px}
/* features */
.feature{top:428px;width:180px;text-align:center}
.feature .icon{width:72px;height:72px;border-radius:50%;background:var(--blue);margin:0 auto;box-shadow:0 0 0 3px #e6ecf6;display:flex;align-items:center;justify-content:center}
.feature h3{font-family:'Open Sans',sans-serif;font-weight:400;font-size:11px;color:var(--ink);margin-top:18px}
.feature p{font-size:6.3px;line-height:11.5px;color:#666;margin-top:8px;padding:0 12px}
/* service */
.service{left:0;top:590px;width:675px;height:218px;background:linear-gradient(90deg,#f3f1f1,#f7f5f5 60%,#f2f0ef)}
.video{left:62px;top:618px;width:227px;height:162px;background:#fff;border:1px solid #ccc}
.video-frame{position:absolute;left:0;top:0;width:225px;height:145px;background:linear-gradient(160deg,#c9d2dc,#a9b5c2 50%,#6f7a88)}
.video-bar{position:absolute;left:0;top:145px;width:225px;height:15px;background:#f2f2f2;display:flex;align-items:center;gap:6px;padding:0 6px;font-size:4.5px;color:#555}
.service-title{left:308px;top:614px;font-family:'Oswald',sans-serif;font-weight:300;font-size:18px;color:var(--ink)}
.service-lead{left:308px;top:642px;font-size:8px;color:var(--blue)}
.service-copy{left:308px;top:661px;width:310px;font-size:6.2px;line-height:11.6px;color:#444}
.service-copy p+p{margin-top:8px}
.service-btn{left:308px;top:760px;width:74px;height:21px}
/* blog */
.section-head{font-family:'Roboto',sans-serif;font-weight:400;font-size:11px;color:var(--blue)}
.post-img{left:56px;width:129px;height:76px;background:linear-gradient(135deg,#d9dee4,#7b8ea5 55%,#3a4a60)}
.post-img.b{background:linear-gradient(135deg,#e9ebee,#b7bcc3 50%,#6b6e74)}
.post{left:199px;width:195px}
.post h4{font-family:'Open Sans',sans-serif;font-weight:400;font-size:9px;color:var(--ink)}
.post .date{font-size:9px;color:var(--ink);margin-top:6px}
.post p{font-size:6.2px;line-height:11.6px;color:#555;margin-top:7px}
.benefits{left:434px;top:829px;width:186px}
.benefits h2{font-family:'Oswald',sans-serif;font-weight:400;font-size:11px;color:var(--blue);padding-bottom:9px;border-bottom:1px solid #e3e3e3}
.benefits ul{list-style:none;margin-top:10px}
.benefits li{position:relative;padding-left:13px;font-size:6.2px;line-height:11.6px;color:#444;margin-bottom:8px}
.benefits li::before{content:"";position:absolute;left:2px;top:3px;width:5px;height:5px;border:1px solid #444;border-radius:50%}
.benefits-btn{left:436px;top:1000px;width:74px;height:21px}
/* footer */
.footer{left:0;top:1054px;width:675px;height:115px;background:var(--light)}
.footer-brand{left:66px;top:1088px;text-align:center;width:112px}
.footer-brand .mark{width:26px;height:26px;background:var(--blue);border-radius:3px;margin:0 auto 6px}
.footer-brand .name{font-family:'Roboto',sans-serif;font-size:13px;color:var(--blue);font-weight:500}
.foot-col h5{font-family:'Roboto',sans-serif;font-weight:400;font-size:9.5px;color:var(--ink)}
.foot-col ul{list-style:none;margin-top:8px}
.foot-col li{font-size:6px;line-height:12px;color:#333}
.follow{display:flex;align-items:center;gap:4px;margin-top:7px;font-size:5px;color:#333}
.follow .pill{width:30px;height:9px;background:#e8e8e8;border:1px solid #bbb;border-radius:2px}
.follow .count{padding:1px 4px;border:1px solid #bbb;border-radius:2px;background:#fff}
.socials{display:flex;gap:3px;margin-top:14px}
.socials span{width:16px;height:16px;border-radius:50%}
.addr{font-size:6.5px;line-height:11px;color:#333;margin-top:6px}
.foot-line{display:flex;align-items:center;gap:8px;font-size:7.5px;color:#333;margin-top:6px}
.foot-line.small{font-size:6.5px;margin-top:4px}
.bottom{left:0;top:1169px;width:675px;height:31px;background:var(--blue);color:var(--white);font-size:6.5px;display:flex;align-items:center;justify-content:center}
</style>
</head>
<body>

<header>
  <div class="abs brand"><span class="brand-mark"></span><span class="brand-name">Meridale PMO</span></div>
  <div class="abs contact-head">
    <div class="phone-ring"><svg width="11" height="11" viewBox="0 0 24 24"><path d="M6.6 10.8a15 15 0 0 0 6.6 6.6l2.2-2.2c.3-.3.7-.4 1-.2 1.1.4 2.3.6 3.6.6.6 0 1 .4 1 1V20c0 .6-.4 1-1 1A17 17 0 0 1 3 4c0-.6.4-1 1-1h3.5c.6 0 1 .4 1 1 0 1.2.2 2.4.6 3.6.1.3 0 .7-.2 1z" fill="#333"/></svg></div>
    <div><div class="ph">Ph: (09) 5550 1928</div><div class="em">enquiries@meridalepmo-example.com</div></div>
  </div>
</header>

<nav class="abs nav">
  <a class="active">HOME</a><a>WHAT IS A PMO</a><a>HOW DOES A PMO</a><a>WHAT'S THE ADVANTAGE</a><a>WHY MERIDALE PMO</a><a>CONTACT US</a>
</nav>

<section>
  <div class="abs hero" role="img" aria-label="Photo of a team of professionals planning on a glass board"></div>
  <h1 class="abs hero-title">Our Team of<br><span class="small">Professionals</span></h1>
  <div class="abs btn hero-btn">GET STARTED NOW</div>
  <div class="abs arrow" style="left:21px"><svg width="8" height="8" viewBox="0 0 10 10"><path d="M7 1 3 5l4 4" stroke="#fff" stroke-width="1.6" fill="none"/></svg></div>
  <div class="abs arrow" style="left:638px"><svg width="8" height="8" viewBox="0 0 10 10"><path d="M3 1l4 4-4 4" stroke="#fff" stroke-width="1.6" fill="none"/></svg></div>
</section>

<section>
  <div class="abs feature" style="left:49px">
    <div class="icon"><svg width="40" height="34" viewBox="0 0 40 34" fill="#fff"><rect x="14" y="2" width="12" height="10" rx="1"/><rect x="7" y="12" width="12" height="10" rx="1"/><rect x="21" y="12" width="12" height="10" rx="1"/><rect x="1" y="22" width="12" height="10" rx="1"/><rect x="14" y="22" width="12" height="10" rx="1"/><rect x="27" y="22" width="12" height="10" rx="1"/></svg></div>
    <h3>Predictable Service</h3>
    <p>Lorem ipsum dolor sit amet, consectetur adipising elit, sed do eiusmod tempor iunt ut labore et dolore magna aliqua. eiusmod</p>
  </div>
  <div class="abs feature" style="left:248px">
    <div class="icon"><svg width="36" height="32" viewBox="0 0 36 32"><path d="M5 22v-6a13 13 0 0 1 26 0v6" stroke="#fff" stroke-width="5" fill="none"/><rect x="3" y="18" width="8" height="12" rx="2" fill="#fff"/><rect x="25" y="18" width="8" height="12" rx="2" fill="#fff"/></svg></div>
    <h3>Consistent Quality</h3>
    <p>Lorem ipsum dolor sit amet, consectetur adipising elit, sed do eiusmod tempor iunt ut labore et dolore magna aliqua. eiusmod</p>
  </div>
  <div class="abs feature" style="left:446px">
    <div class="icon"><svg width="24" height="36" viewBox="0 0 24 36"><path d="M19 9c-2-2-4-3-7-3-4 0-6 2-6 5 0 7 13 4 13 12 0 3-3 6-7 6-3 0-6-1-8-4M12 2v32" stroke="#fff" stroke-width="3.5" fill="none"/></svg></div>
    <h3>Competitive Price</h3>
    <p>Lorem ipsum dolor sit amet, consectetur adipising elit, sed do eiusmod tempor iunt ut labore et dolore magna aliqua. eiusmod</p>
  </div>
</section>

<section>
  <div class="abs service"></div>
  <div class="abs video">
    <div class="video-frame" role="img" aria-label="Video still of colleagues meeting around a laptop">
      <svg style="position:absolute;left:93px;top:53px" width="40" height="40" viewBox="0 0 40 40"><circle cx="20" cy="20" r="19" fill="rgba(255,255,255,.55)"/><path d="M15 11l14 9-14 9z" fill="#222"/></svg>
    </div>
    <div class="video-bar">
      <svg width="5" height="5" viewBox="0 0 5 5"><path d="M0 0l5 2.5L0 5z" fill="#222"/></svg>
      <span style="margin-left:6px">10:00/05:03</span>
      <svg width="113" height="3" style="margin-left:18px"><rect width="113" height="2" fill="#555"/><rect width="55" height="2" fill="#d9452e"/></svg>
      <svg width="8" height="6" viewBox="0 0 8 6" style="margin-left:8px"><path d="M0 2h2l2-2v6L2 4H0z" fill="#222"/><path d="M5.5 1.5a2 2 0 0 1 0 3" stroke="#222" fill="none" stroke-width=".8"/></svg>
      <svg width="22" height="2"><rect width="22" height="2" fill="#d9452e"/></svg>
    </div>
  </div>
  <h2 class="abs service-title">Portfolio Management Office As A Service</h2>
  <div class="abs service-lead">Meridale PMO offers a competitive alternative to traditional in-house PMOs.</div>
  <div class="abs service-copy">
    <p>Our team of professionals comes equipped with a wealth of experience in both private and public sectors. Let our professionally certified experts monitor and improve your project management so that you can focus on your business.</p>
    <p>We aim to align the selection and execution of projects and programs with your organization's business goals, thereby increasing the success of project execution. We provide coordination, guidance, and training to your project. Most importantly, we work with you to implement these strategies in a way that works with your</p>
  </div>
  <div class="abs btn service-btn">READ MORE</div>
</section>

<section>
  <h2 class="abs section-head" style="left:54px;top:828px">RECENT BLOG</h2>
  <div class="abs post-img" style="top:857px" role="img" aria-label="Photo of businessmen reviewing a tablet"></div>
  <div class="abs post" style="top:853px">
    <h4>Sed ut perspiciatis unde omnis iste</h4>
    <div class="date">April 25, 2015</div>
    <p>Lorem ipsum dolor sit amet, consectetur adipiscing elit, sed do eiusmod tempor incididunt ut labore et dolore magna aliqua. Ut enim ad minim veniam, quis nostrud exercitation ullamco laboris nisi ut aliquip ex ea commodo consequat.</p>
  </div>
  <div class="abs post-img b" style="top:949px" role="img" aria-label="Photo of a businessman with a city skyline illustration"></div>
  <div class="abs post" style="top:945px">
    <h4>Sed ut perspiciatis unde omnis iste</h4>
    <div class="date">April 25, 2015</div>
    <p>Lorem ipsum dolor sit amet, consectetur adipiscing elit, sed do eiusmod tempor incididunt ut labore et dolore magna aliqua. Ut enim ad minim veniam, quis nostrud exercitation ullamco laboris nisi ut aliquip ex ea commodo consequat.</p>
  </div>

  <div class="abs benefits">
    <h2>MERIDALE PMO WILL ALLOW YOU TO :</h2>
    <ul>
      <li>Optimize the use of your capital. We'll help you avoid project inefficiency and maximize success by choosing the right projects the first time, every time.</li>
      <li>Filter out the noise; you have enough on your plate without being inundated with data. We'll communicate efficiently to provide you with the important information you need.</li>
      <li>Let Project Managers focus on what they know best-- project outcomes.They won't have be burdened with administration.</li>
    </ul>
  </div>
  <div class="abs btn benefits-btn">READ MORE</div>
</section>

<footer>
  <div class="abs footer"></div>
  <div class="abs footer-brand"><div class="mark"></div><div class="name">Meridale PMO</div></div>
  <div class="abs foot-col" style="left:213px;top:1066px">
    <h5>Quick Links</h5>
    <ul><li>What is a PMO</li><li>How does a PMO add value</li><li>What's the Advantage</li><li>Why Meridale PMO</li><li>Contact us</li><li>Blog</li></ul>
  </div>
  <div class="abs foot-col" style="left:343px;top:1066px">
    <h5>Connect With US</h5>
    <div class="follow" style="margin-top:10px"><span class="pill"></span><span class="count">@Meridale PMO</span></div>
    <div class="follow"><span class="pill"></span><span class="count">105</span></div>
    <div class="socials"><span style="background:#3b5a98"></span><span style="background:#2aa3e0"></span><span style="background:#333"></span><span style="background:#f0691f"></span><span style="background:#d9232d"></span></div>
  </div>
  <div class="abs foot-col" style="left:494px;top:1066px">
    <h5>Contact Us</h5>
    <div class="addr">42-48 Meridale Street<br>Harbourvale, QLD, 4391</div>
    <div class="foot-line" style="margin-top:10px"><svg width="10" height="10" viewBox="0 0 24 24"><path d="M6.6 10.8a15 15 0 0 0 6.6 6.6l2.2-2.2c.3-.3.7-.4 1-.2 1.1.4 2.3.6 3.6.6.6 0 1 .4 1 1V20c0 .6-.4 1-1 1A17 17 0 0 1 3 4c0-.6.4-1 1-1h3.5c.6 0 1 .4 1 1 0 1.2.2 2.4.6 3.6.1.3 0 .7-.2 1z" fill="none" stroke="#1a5bc4" stroke-width="1.8"/></svg>TOLL FREE:&nbsp; (09) 5550 1928</div>
    <div class="foot-line small"><svg width="10" height="8" viewBox="0 0 10 8"><rect x=".5" y=".5" width="9" height="7" fill="none" stroke="#1a5bc4"/><path d="M.5 .5 5 4.5 9.5.5" fill="none" stroke="#1a5bc4"/></svg>info@meridalepmo-example.com.au</div>
  </div>
  <div class="abs bottom">2015 All Right Reserved. Meridale PMO</div>
</footer>

</body>
</html>
```